Construction material supplies company business card ****

1. Full company name “Marlow Aggregate Products Ltd”
I am after a Business card design for the company as a whole. We are better known in Solomon Islands as “Marlow Aggregate” for short.

We are a building materials supplier of
Ready Mixed Concrete, Bricks and Blocks,
Quarry products- gravel, aggregates, sand etc.
Cement distributor/retailer of reputable brands.
Other prefab concrete products. Culverts, wave breakers, concrete retaining blocks etc.

2. Competitive Advantage over Competition: Quality, efficient, professional, dependable, reliable

3. We want people to feel trust worthy, high quality, strong when they see our brand

5. No preference to color. Maybe more sturdy and corporate. Not fancy.

Industry/Entity Type

CONSTRUCTION SUPPLY

Contact Information for Business Card

Name, Position, office phone mob phone, email

Requirements
Must have
• the company logo
Nice to have
• would like to see a mixture of designs, of with logo only and also with simple graphic designs to bring out the company whilst still have the strong sturdy professional feeling

```html
<!DOCTYPE html>
<html lang="en">
<head>
<meta charset="utf-8">
<title>Marlow Aggregate – Business Card</title>
<link href="https://fonts.googleapis.com/css2?family=Arimo:wght@400;700&display=swap" rel="stylesheet">
<style>
  :root {
    --backdrop: #e4e4e2;
    --navy: #1d4568;
    --navy-deep: #163a5a;
    --paper: #ffffff;
    --ink-grey: #6f6f6f;
    --rule-grey: #8a8a8a;
  }
  * { box-sizing: border-box; margin: 0; padding: 0; }
  html, body {
    width: 1200px; height: 801px; overflow: hidden;
    background: var(--backdrop);
    font-family: "Arimo", Arial, sans-serif;
  }
  .stage {
    position: relative; width: 1200px; height: 801px;
    display: flex; align-items: center; justify-content: center; gap: 40px;
  }
  .card {
    position: relative; width: 540px; height: 309px;
    box-shadow: 0 10px 24px rgba(0,0,0,0.18);
    overflow: hidden;
  }

  /* Front side */
  .card--front { background: var(--navy); }
  .front-brand {
    position: absolute; right: 40px; bottom: 46px;
    display: flex; align-items: center; gap: 12px;
    color: var(--paper); font-weight: 700; font-size: 30px;
    letter-spacing: 1px; text-transform: uppercase;
  }
  .brand-square {
    width: 18px; height: 18px; background: currentColor; flex: none;
  }

  /* Back side */
  .card--back {
    background: var(--paper);
    border-left: 4px solid var(--navy);
    border-bottom: 4px solid var(--navy);
  }
  .back-brand {
    position: absolute; right: 34px; top: 62px;
    display: flex; align-items: center; gap: 10px;
    color: var(--navy); font-weight: 700; font-size: 27px;
    letter-spacing: 1px; text-transform: uppercase;
  }
  .brand-rule {
    position: absolute; left: 30px; right: 30px; top: 150px;
    border-top: 1px solid var(--rule-grey);
  }
  .person { position: absolute; left: 30px; top: 160px; }
  .person-name {
    color: var(--navy); font-weight: 700; font-size: 19px;
    text-transform: uppercase; letter-spacing: 0.3px;
  }
  .person-role { color: var(--ink-grey); font-size: 15px; margin-top: 2px; }
  .person-rule { width: 200px; border-top: 1px solid var(--rule-grey); margin-top: 6px; }
  .contact-list { list-style: none; margin-top: 10px; }
  .contact-list li {
    display: flex; align-items: center; gap: 10px;
    color: var(--ink-grey); font-size: 15px; line-height: 22px;
  }
  .contact-icon { width: 14px; height: 14px; fill: var(--navy); flex: none; }
  .address {
    position: absolute; right: 34px; top: 170px;
    text-align: right; color: var(--ink-grey); font-size: 14px; line-height: 18px;
  }
</style>
</head>
<body>
<main class="stage">
  <section class="card card--front" aria-label="Card front">
    <div class="front-brand"><span class="brand-square"></span>Marlow Aggregate</div>
  </section>

  <section class="card card--back" aria-label="Card back">
    <div class="back-brand"><span class="brand-square"></span>Marlow Aggregate</div>
    <div class="brand-rule"></div>
    <div class="person">
      <p class="person-name">Daniel Reeve</p>
      <p class="person-role">Manager</p>
      <div class="person-rule"></div>
      <ul class="contact-list">
        <li>
          <svg class="contact-icon" viewBox="0 0 24 24" aria-hidden="true"><path d="M6.6 10.8a15.1 15.1 0 0 0 6.6 6.6l2.2-2.2c.3-.3.7-.4 1-.2 1.1.4 2.3.6 3.6.6.6 0 1 .4 1 1V20c0 .6-.4 1-1 1A17 17 0 0 1 3 4c0-.6.4-1 1-1h3.5c.6 0 1 .4 1 1 0 1.3.2 2.5.6 3.6.1.3 0 .7-.2 1z"/></svg>
          123-456-2100
        </li>
        <li>
          <svg class="contact-icon" viewBox="0 0 24 24" aria-hidden="true"><path d="M2 5h20v14H2z M3.5 6.5 12 13l8.5-6.5" stroke="#fff" stroke-width="1.5"/></svg>
          youremail@mailbox.com
        </li>
        <li>
          <svg class="contact-icon" viewBox="0 0 24 24" aria-hidden="true"><circle cx="12" cy="12" r="10"/><path d="M2 12h20M12 2c3 3 3 17 0 20M12 2c-3 3-3 17 0 20" stroke="#fff" stroke-width="1.5" fill="none"/></svg>
          www.yourwebsite.com
        </li>
      </ul>
    </div>
    <p class="address">Your address, city<br>state, ZIP 0000</p>
  </section>
</main>
</body>
</html>
```